Tovane and Partners Business Card

A business card that can be templates for all employees using our newly created logo and information. We are looking for stylish however simplistic in nature, clean looks are better than over the top, however creativity will be appreciated if it has the right appeal. Note: If you feel a type of card (plastic, metalic, carbon, raised lettering, etc) helps your design please specify.
Target Market(s)
Investigation ETC
Industry/Entity Type
Private Investigator
Contact Information for Business Card
Dan Moskel
President
5173 Wexmoor Lane
Hermitage PA 16203-4419
Cell: 724-555-0193; Office: 724-555-0147
Email: danmoskel@tovanepartners-example.com
Requirements
Must have
- Website TovanePartners-example.com
- Name, address, phone number ETC
- Use of current Logo and color pallets if applicable
- TM By logo, small

Nice to have
- Would like to see with and without a photo on the design

Should not have
- Redesign of logo, changing of colors

```html
<!DOCTYPE html>
<html lang="en">
<head>
<meta charset="utf-8">
<title>Tovane and Partners Business Card</title>
<link rel="stylesheet" href="https://fonts.googleapis.com/css2?family=Cinzel:wght@400;600&family=Tinos:wght@400;700&display=swap">
<style>
  :root {
    --backdrop: #ecebe8;
    --card-top: #141a24;
    --card-bottom: #0b0e15;
    --white: #ffffff;
    --brand-red: #e8452a;
    --brand-orange: #f58b1f;
    --brand-blue: #0a84f0;
    --brand-green: #3cb814;
    --edge-red: #d41f12;
    --photo-dark: #1e222b;
    --photo-mid: #566a88;
  }
  html, body {
    margin: 0;
    width: 1200px;
    height: 1200px;
    overflow: hidden;
    background: var(--backdrop);
  }
  p { margin: 0; }
  .canvas { position: relative; width: 1200px; height: 1200px; }
  .card {
    position: absolute;
    width: 780px;
    height: 445px;
    background: linear-gradient(160deg, var(--card-top), var(--card-bottom));
    overflow: hidden;
    box-shadow: 0 6px 18px rgba(0,0,0,0.25);
  }
  .card-front { left: 209px; top: 140px; }
  .card-back { left: 211px; top: 649px; }

  .brand {
    position: absolute;
    left: 0; right: 0; top: 178px;
    display: flex;
    justify-content: center;
    align-items: center;
    gap: 12px;
  }
  .brand-dot {
    width: 30px; height: 30px;
    border-radius: 50%;
    background: var(--brand-red);
  }
  .brand-name {
    font-family: "Tinos", serif;
    font-weight: 700;
    font-size: 30px;
    letter-spacing: 1px;
    color: var(--brand-red);
    text-transform: uppercase;
  }
  .tagline {
    position: absolute;
    left: 0; right: 0; top: 273px;
    text-align: center;
    font-family: "Cinzel", serif;
    font-size: 19px;
    line-height: 24px;
    letter-spacing: 5px;
    color: var(--white);
  }
  .colour-bar {
    position: absolute;
    left: 0; right: 0; bottom: 0;
    height: 13px;
    display: flex;
  }
  .colour-bar span { flex: 1; }
  .c-red { background: var(--brand-red); }
  .c-orange { background: var(--brand-orange); }
  .c-blue { background: var(--brand-blue); }
  .c-green { background: var(--brand-green); }

  .icon-rail {
    position: absolute;
    left: 0; top: 67px;
    width: 75px;
    height: 334px;
    display: flex;
    flex-direction: column;
  }
  .icon-tile {
    height: 83.5px;
    display: flex;
    align-items: center;
    justify-content: center;
    box-shadow: inset -5px 0 0 rgba(0,0,0,0.18);
  }
  .icon-tile svg { width: 28px; height: 28px; fill: var(--white); }
  .icon-tile.c-red { box-shadow: inset -5px 0 0 var(--edge-red); }

  .contact {
    position: absolute;
    font-family: "Tinos", serif;
    font-size: 20px;
    line-height: 25px;
    color: var(--white);
    white-space: nowrap;
  }
  .contact-email { top: 96px; left: 108px; }
  .contact-phone { top: 168px; left: 111px; }
  .contact-address { top: 253px; left: 112px; }
  .contact-web { top: 343px; left: 113px; }

  .portrait {
    position: absolute;
    left: 497px; top: 94px;
    width: 164px; height: 164px;
    border-radius: 50%;
    border: 4px solid var(--brand-red);
    background: radial-gradient(circle at 50% 45%, var(--photo-mid), var(--photo-dark) 70%);
  }
  .person {
    position: absolute;
    left: 470px; width: 240px;
    top: 288px;
    text-align: center;
    font-family: "Tinos", serif;
    color: var(--white);
  }
  .person-name { font-size: 32px; line-height: 36px; }
  .person-role { font-size: 20px; line-height: 22px; margin-left: -12px; }
</style>
</head>
<body>
<main class="canvas">
  <section class="card card-front" aria-label="Card front">
    <div class="brand">
      <span class="brand-dot"></span>
      <span class="brand-name">Tovane and Partners</span>
    </div>
    <p class="tagline">FIRE INVESTIGATION</p>
    <div class="colour-bar">
      <span class="c-red"></span><span class="c-orange"></span><span class="c-blue"></span><span class="c-green"></span>
    </div>
  </section>

  <section class="card card-back" aria-label="Card back">
    <div class="icon-rail">
      <div class="icon-tile c-red">
        <svg viewBox="0 0 24 24" aria-hidden="true"><path d="M2 5h20v14H2z M3.5 6.5v.4l8.5 6 8.5-6v-.4z" fill-rule="evenodd"/></svg>
      </div>
      <div class="icon-tile c-orange">
        <svg viewBox="0 0 24 24" aria-hidden="true"><path d="M6.6 2.5l3 3.3-1.8 2.6c1 2.3 3.3 4.8 5.8 6l2.6-1.8 3.3 3-1.6 3.4C11 18.5 5.4 12.9 3.2 4.1z"/></svg>
      </div>
      <div class="icon-tile c-blue">
        <svg viewBox="0 0 24 24" aria-hidden="true"><path d="M12 3L1.5 12h3v9h6v-6h3v6h6v-9h3z"/></svg>
      </div>
      <div class="icon-tile c-green">
        <svg viewBox="0 0 24 24" aria-hidden="true"><circle cx="12" cy="12" r="10"/><path d="M7 6c2 1 3 2 2 4s-3 1-3 3 2 3 3 5l-1 2C4.5 18 3 15 3.4 11 4 8.5 5.2 6.8 7 6zm8-2c1.5.5 3 1.6 4 3l-2 1-1 3 2 2 1.5-.5c-.2 2-1 3.5-2.5 5l-1-3-2-1v-3l-2-1 1-3z" fill="#3cb814"/></svg>
      </div>
    </div>

    <p class="contact contact-email">danmoskel@tovanepartners-example.com</p>
    <p class="contact contact-phone">724-555-0193<br>724-555-0147</p>
    <p class="contact contact-address">5173 Wexmoor Lane<br>Carrowfield PA 16203-4419</p>
    <p class="contact contact-web">www.TovanePartners-example.com</p>

    <div class="portrait" role="img" aria-label="Portrait photo of Dan Moskel"></div>
    <div class="person">
      <div class="person-name">Dan Moskel</div>
      <div class="person-role">President</div>
    </div>
  </section>
</main>
</body>
</html>
```